Our swimming pool service needs your help with letterhead

Letterhead for small swimming pool service- We would like a professional look with a creative layout- must be compatible with LedgerNest forms (sample attached)
No more than 2 colors in graphics

Target Market(s)

Homeowners/ Contractors

Font styles to use
Sans Serif

Colors
33a6d7
85cae6

Requirements
Must have
• Logo (file attached)
• Compatible with LedgerNest (sample attached)
• Mailing address- P.O. Box 58, Cedar Hollow NY 11592
• phone- (631) 529-6180
• email- marcdoylewater@mailbrook.net
• Licensed & Insured
Nice to have
• Small slogan- Examples:Family owned and operated for 25 years, 25 years of trusted service
• Creative layout
Should not have
• Blue color must be same as blue in our logo
• No thick lines of color
• No design in middle of page

```html
<!DOCTYPE html>
<html lang="en">
<head>
<meta charset="utf-8">
<title>Marc Doyle Pool Service – Invoice Letterhead</title>
<link rel="stylesheet" href="https://fonts.googleapis.com/css2?family=Roboto:wght@400;500;700&family=Cinzel:wght@600&display=swap">
<style>
  :root {
    --backdrop: #eceef0;
    --paper: #f3f4f5;
    --navy: #1f3354;
    --logo-blue: #33a6d7;
    --light-blue: #85cae6;
    --cell: #dfe4ea;
    --rule: #b9c0c8;
    --ink: #2a3a8c;
    --text: #2b3441;
    --stamp: #c8232c;
  }
  * { box-sizing: border-box; margin: 0; padding: 0; }
  html, body { width: 1200px; height: 795px; overflow: hidden; }
  body {
    background: var(--backdrop);
    font-family: "Roboto", Arial, sans-serif;
    color: var(--text);
    position: relative;
  }
  .letterhead {
    position: absolute;
    left: 300px; top: 10px;
    width: 600px; height: 776px;
    background: var(--paper);
    box-shadow: 0 2px 10px rgba(0,0,0,.08);
    overflow: hidden;
  }
  .brand {
    position: absolute; left: 40px; top: 46px;
    display: flex; align-items: center; gap: 10px;
  }
  .brand-mark {
    width: 30px; height: 30px; border-radius: 50%;
    background: var(--logo-blue);
    flex: none;
  }
  .brand-name {
    font-family: "Cinzel", Georgia, serif;
    font-weight: 600; color: var(--navy);
    font-size: 20px; line-height: 1.1; letter-spacing: .5px;
  }
  .brand-rule {
    position: absolute; left: 40px; top: 104px;
    width: 250px; height: 1px; background: var(--rule);
  }
  .header-divider {
    position: absolute; left: 300px; top: 36px;
    width: 1px; height: 60px; background: var(--rule);
  }
  .contact {
    position: absolute; left: 318px; top: 40px;
    list-style: none; font-size: 10px; line-height: 15px; color: var(--text);
  }
  .contact li { display: flex; align-items: center; gap: 6px; white-space: nowrap; }
  .contact .dot {
    width: 8px; height: 8px; border-radius: 50%; background: var(--logo-blue);
    flex: none;
  }
  .bill-to {
    position: absolute; left: 40px; top: 150px;
    width: 260px; height: 112px;
    border: 1px solid var(--rule);
  }
  .bill-to h2 {
    background: var(--cell); font-size: 10px; font-weight: 700;
    padding: 6px 10px; letter-spacing: .3px; color: var(--navy);
  }
  .bill-to address {
    font-style: normal; font-size: 10.5px; line-height: 14px;
    color: var(--ink); padding: 10px 12px;
  }
  .paid-stamp {
    position: absolute; left: 314px; top: 124px;
    width: 56px; height: 56px; border-radius: 50%;
    background: var(--stamp); opacity: .85;
  }
  .invoice-meta {
    position: absolute; left: 380px; top: 178px;
    width: 180px; border-collapse: collapse; font-size: 10px;
  }
  .invoice-meta th {
    background: var(--cell); font-weight: 700; color: var(--navy);
    padding: 6px 8px; text-align: left; border: 1px solid var(--rule);
    white-space: nowrap;
  }
  .invoice-meta td {
    padding: 6px 8px; color: var(--ink); border: 1px solid var(--rule);
    white-space: nowrap;
  }
  .line-items {
    position: absolute; left: 40px; top: 288px;
    width: 520px; border-collapse: collapse; font-size: 10px;
    table-layout: fixed;
  }
  .line-items th {
    background: var(--cell); font-weight: 700; color: var(--navy);
    text-align: left; padding: 7px 8px; border: 1px solid var(--rule);
  }
  .line-items td {
    vertical-align: top; padding: 10px 8px; color: var(--ink);
    border-left: 1px solid var(--rule); border-right: 1px solid var(--rule);
    border-bottom: 1px solid var(--rule);
    height: 340px; line-height: 16px; font-size: 11px;
  }
  .line-items td.num { font-size: 10px; }
  .summary {
    position: absolute; left: 40px; top: 655px;
    width: 520px; display: flex; height: 30px; font-size: 10.5px;
  }
  .summary .payable {
    flex: 1; background: var(--cell); border: 1px solid var(--rule);
    display: flex; align-items: center; padding: 0 10px;
    font-weight: 700; color: var(--navy);
  }
  .summary .total-label, .summary .total-value {
    border: 1px solid var(--rule); border-left: none;
    display: flex; align-items: center; justify-content: center;
    font-weight: 700; color: var(--navy);
  }
  .summary .total-label { width: 70px; background: var(--cell); }
  .summary .total-value { width: 70px; font-size: 12px; }
  .slogan-band {
    position: absolute; left: 0; bottom: 22px;
    width: 100%; height: 28px; background: var(--navy);
    color: #fff; font-size: 12px; letter-spacing: .6px;
    display: flex; align-items: center; justify-content: center;
    border-bottom: 3px solid var(--light-blue);
  }
  .slogan-band strong { margin-left: 4px; font-weight: 700; }
</style>
</head>
<body>
  <main class="letterhead">
    <header>
      <div class="brand">
        <span class="brand-mark"></span>
        <div class="brand-name">Marc Doyle<br>Pool Service</div>
      </div>
      <div class="brand-rule"></div>
      <div class="header-divider"></div>
      <ul class="contact">
        <li><span class="dot"></span>P.O. Box 58, Cedar Hollow NY 11592</li>
        <li><span class="dot"></span>(631) 529-6180</li>
        <li><span class="dot"></span>marcdoylewater@mailbrook.net</li>
        <li><span class="dot"></span>Licensed &amp; Insured</li>
      </ul>
    </header>

    <section class="bill-to">
      <h2>BILL TO:</h2>
      <address>
        BRIGHTLINE BUILDERS CO<br>
        PO BOX 2207, Elm Street,<br>
        Ohio 43118-0925,USA
      </address>
    </section>

    <div class="paid-stamp" role="img" aria-label="Red paid stamp"></div>

    <table class="invoice-meta">
      <tr><th>INVOICE NO.</th><th>TERMS</th></tr>
      <tr><td>000001</td><td>Due On Receipt</td></tr>
    </table>

    <table class="line-items">
      <colgroup>
        <col style="width:78px"><col style="width:252px"><col style="width:56px"><col style="width:64px"><col style="width:70px">
      </colgroup>
      <thead>
        <tr><th>DATE</th><th>ITEM DESCRIPTION</th><th>QTY</th><th>RATE</th><th>AMOUNT</th></tr>
      </thead>
      <tbody>
        <tr>
          <td class="num">19/09/12</td>
          <td>Labor<br>Sales Tax</td>
          <td></td>
          <td class="num">0.00<br>8.625%</td>
          <td class="num">0.00T<br>0.00</td>
        </tr>
      </tbody>
    </table>

    <div class="summary">
      <div class="payable">Check Payable To Marc Doyle. CHARGE BY PHONE.</div>
      <div class="total-label">TOTAL</div>
      <div class="total-value">$0.00</div>
    </div>

    <footer class="slogan-band">FAMILY OWNED AND OPERATED FOR <strong>25 YEARS</strong></footer>
  </main>
</body>
</html>
```